Business Card *

A business card design
Use the logo uploaded in the brief page.
You may use placeholders in your design layouts.
I will provide the actual business card details to the winning designer.

Logo
Place for contact info (name, title, phone, email, etc)

Requirements
Must have
• Logo

```html
<!DOCTYPE html>
<html lang="en">
<head>
<meta charset="utf-8">
<title>Fernbrook Business Card</title>
<link href="https://fonts.googleapis.com/css2?family=Montserrat:wght@400;500;800&display=swap" rel="stylesheet">
<style>
  :root {
    --backdrop: #d4d3cf;
    --card-white: #ffffff;
    --brand-green: #3cb64b;
    --leaf-green: #8cc63f;
    --text-dark: #3a3a3a;
    --brand-grey: #8e8e8e;
    --rule-green: #8cc63f;
  }
  * { box-sizing: border-box; margin: 0; padding: 0; }
  html, body {
    width: 1200px; height: 801px; overflow: hidden;
    background: var(--backdrop);
    font-family: "Montserrat", Arial, sans-serif;
  }
  .stage {
    position: relative; width: 1200px; height: 801px;
    display: flex; align-items: center; justify-content: center; gap: 40px;
  }
  .card {
    position: relative; width: 525px; height: 300px;
    box-shadow: 0 6px 18px rgba(0,0,0,0.18);
  }
  .card--front { background: var(--card-white); }
  .card--back {
    background: var(--brand-green);
    display: flex; flex-direction: column; align-items: center; justify-content: center;
    color: var(--card-white);
  }

  /* brand lockup */
  .brand { display: flex; align-items: center; gap: 10px; }
  .brand__dot {
    width: 40px; height: 40px; border-radius: 50%; flex: none;
    background: var(--brand-grey);
  }
  .brand__text { font-weight: 800; color: var(--brand-grey); line-height: 1; }
  .brand__name { font-size: 24px; letter-spacing: 0.3px; }
  .brand__tag { font-size: 7.5px; letter-spacing: 1.6px; margin-top: 5px; }

  .card--front .brand { position: absolute; left: 30px; top: 70px; }

  .card--back .brand { flex-direction: column; gap: 18px; }
  .card--back .brand__dot {
    width: 96px; height: 96px; background: transparent;
    border: 10px solid var(--card-white);
  }
  .card--back .brand__text { color: var(--card-white); text-align: center; }
  .card--back .brand__name { font-size: 52px; letter-spacing: 1px; }
  .card--back .brand__tag { font-size: 15px; letter-spacing: 4px; margin-top: 8px; }

  /* person */
  .person {
    position: absolute; right: 32px; top: 34px; text-align: right;
  }
  .person__name { font-weight: 800; font-size: 19px; letter-spacing: 0.5px; white-space: nowrap; }
  .person__first { color: var(--brand-green); }
  .person__last { color: var(--leaf-green); }
  .person__title { font-size: 11.5px; color: var(--text-dark); margin-top: 4px; }

  .divider {
    position: absolute; left: 30px; right: 30px; top: 136px;
    height: 1px; background: var(--rule-green);
  }

  /* contact */
  .contact {
    position: absolute; left: 30px; top: 156px;
    font-size: 12.5px; color: var(--text-dark); line-height: 1.6;
    list-style: none;
  }
  .contact__row { display: flex; align-items: center; gap: 7px; }
  .contact__row--plain { padding-left: 19px; }
  .contact__icon { width: 12px; height: 12px; flex: none; }
  .contact__accent { color: var(--leaf-green); }
</style>
</head>
<body>
<main class="stage">

  <section class="card card--front">
    <div class="brand">
      <span class="brand__dot"></span>
      <div class="brand__text">
        <div class="brand__name">FERNBROOK</div>
        <div class="brand__tag">AGRICULTURE AND INDUSTRY</div>
      </div>
    </div>

    <div class="person">
      <div class="person__name"><span class="person__first">DALEN</span> <span class="person__last">MORROW</span></div>
      <div class="person__title">Owner/CEO</div>
    </div>

    <div class="divider"></div>

    <ul class="contact">
      <li class="contact__row contact__row--plain"><span>418 W Alder Road</span></li>
      <li class="contact__row contact__row--plain"><span>Harlow County Name 7702</span></li>
      <li class="contact__row">
        <svg class="contact__icon" viewBox="0 0 12 12"><circle cx="6" cy="6" r="6" fill="#3cb64b"/><path d="M4 3.2l1 1.6-.6.7c.4.8 1 1.4 1.8 1.8l.7-.6 1.6 1-.6 1.1C5.7 8.7 3.3 6.3 3 4z" fill="#fff"/></svg>
        <span>123-608-31475</span>
      </li>
      <li class="contact__row">
        <svg class="contact__icon" viewBox="0 0 12 12"><rect x="0" y="2" width="12" height="8.5" rx="1" fill="#3cb64b"/><path d="M0.8 2.8L6 7l5.2-4.2" stroke="#fff" stroke-width="1" fill="none"/></svg>
        <span>info@fernbrookagric.com</span>
      </li>
      <li class="contact__row">
        <svg class="contact__icon" viewBox="0 0 12 12"><circle cx="6" cy="6" r="6" fill="#3cb64b"/><ellipse cx="6" cy="6" rx="2.4" ry="5.4" stroke="#fff" stroke-width=".8" fill="none"/><path d="M.8 6h10.4" stroke="#fff" stroke-width=".8"/></svg>
        <span>www.<span class="contact__accent">fernbrookagric</span>.com</span>
      </li>
    </ul>
  </section>

  <section class="card card--back">
    <div class="brand">
      <span class="brand__dot"></span>
      <div class="brand__text">
        <div class="brand__name">FERNBROOK</div>
        <div class="brand__tag">AGRICULTURE AND INDUSTRY</div>
      </div>
    </div>
  </section>

</main>
</body>
</html>
```